Price Trend Graphic for Estimates

I want to add a graphic to my estimates that shows the projected price trend of the work we are quoting to the customer. I have attached a couple ideas I was working on but they are garbage. Hopefully you can see the intent and make it look a lot better. Basically I want the customer to see a really a professional / technological graphic that will stimulate them to purchase Right Now! before the price goes up further. So maybe if the "Today's Price" looks nice and friendly and then becomes more critical and ominous as it goes forward 30 days.... 90 days.... Idea is to psychologically

Target Market(s)

Customers for our Construction business

Industry/Entity Type

Construction

Colors
0054AA
0677BA
7BADD7
CADEEF
E8F1F8
0094D4
00A9DD
6FCCEA
C7EBF8
E9F6FB
FFF300
FFF600
FEFA6F
FFFEC7
FFFEE8
F0912C
F2A743
F7CA91
FBE8D2
FDF5EE

Requirements
Must have
• nice looking graphic with upwards moving arrow and 3 price points
Nice to have
• technological / modern looking chart

```html
<!DOCTYPE html>
<html lang="en">
<head>
<meta charset="utf-8">
<title>Price Trend Graphic</title>
<link href="https://fonts.googleapis.com/css2?family=Poppins:wght@300;400;600;700&display=swap" rel="stylesheet">
<style>
  :root {
    --left-bg: #0b0b0b;
    --card-bg: #1e1e1e;
    --right-bg: #0a0a16;
    --ring: rgba(255,255,255,0.05);
    --white: #ffffff;
    --muted: #bdbdbd;
    --dim: #9a9a9a;
    --teal-1: #12b3a8;
    --teal-2: #3dd09b;
    --amber-1: #d29a24;
    --amber-2: #bda45e;
    --red-1: #9e2530;
    --red-2: #b83a44;
    --trend-pink: #e23a66;
    --trend-red: #b0213a;
    --orange: #f2a743;
  }
  html, body {
    margin: 0;
    padding: 0;
    width: 1200px;
    height: 426px;
    overflow: hidden;
    background: var(--left-bg);
  }
  .canvas {
    display: block;
    width: 1200px;
    height: 426px;
    font-family: 'Poppins', sans-serif;
  }
  .axis-label { fill: var(--white); font-size: 13px; font-weight: 400; }
  .trend-label { fill: var(--white); font-size: 13px; font-weight: 400; }
  .trend-label--bold { font-weight: 600; }
  .headline { fill: var(--white); font-size: 19px; font-weight: 300; }
  .headline--strong { font-weight: 700; }
  .stage-name { font-weight: 700; }
  .stage-sub { font-weight: 400; }
  .price { font-weight: 700; }
</style>
</head>
<body>
<svg class="canvas" viewBox="0 0 1559 554" xmlns="http://www.w3.org/2000/svg" role="img" aria-label="Projected price trend: today $6,500, in 30 days $7,280, in 90 days $7,460">
  <defs>
    <linearGradient id="teal-fill" x1="0" y1="0" x2="1" y2="1">
      <stop offset="0" stop-color="var(--teal-1)"/>
      <stop offset="1" stop-color="var(--teal-2)"/>
    </linearGradient>
    <linearGradient id="amber-fill" x1="0" y1="0" x2="1" y2="1">
      <stop offset="0" stop-color="var(--amber-1)"/>
      <stop offset="1" stop-color="var(--amber-2)"/>
    </linearGradient>
    <linearGradient id="red-fill" x1="0" y1="0" x2="1" y2="1">
      <stop offset="0" stop-color="var(--red-1)"/>
      <stop offset="1" stop-color="var(--red-2)"/>
    </linearGradient>
    <linearGradient id="bar-teal" x1="0" y1="0" x2="0" y2="1">
      <stop offset="0" stop-color="#1f4a44"/>
      <stop offset="1" stop-color="#1c302d"/>
    </linearGradient>
    <linearGradient id="bar-amber" x1="0" y1="0" x2="0" y2="1">
      <stop offset="0" stop-color="#4a3a1c"/>
      <stop offset="1" stop-color="#302a20"/>
    </linearGradient>
    <linearGradient id="bar-red" x1="0" y1="0" x2="0" y2="1">
      <stop offset="0" stop-color="#4a1f25"/>
      <stop offset="1" stop-color="#2e2022"/>
    </linearGradient>
    <linearGradient id="trend-left" x1="120" y1="0" x2="650" y2="0" gradientUnits="userSpaceOnUse">
      <stop offset="0" stop-color="var(--trend-pink)"/>
      <stop offset="0.4" stop-color="#e0406a"/>
      <stop offset="1" stop-color="#a8354f"/>
    </linearGradient>
    <linearGradient id="trend-right" x1="898" y1="0" x2="1428" y2="0" gradientUnits="userSpaceOnUse">
      <stop offset="0" stop-color="#0f8f86"/>
      <stop offset="0.27" stop-color="#2bbf9a"/>
      <stop offset="0.52" stop-color="var(--orange)"/>
      <stop offset="0.75" stop-color="#d9473a"/>
      <stop offset="1" stop-color="var(--trend-red)"/>
    </linearGradient>
  </defs>

  <!-- Left panel: axis chart -->
  <g class="panel panel--chart">
    <rect x="0" y="0" width="780" height="554" fill="var(--left-bg)"/>
    <circle cx="145" cy="30" r="70" fill="none" stroke="var(--ring)" stroke-width="22"/>
    <rect class="chart-card" x="37" y="27" width="706" height="500" rx="12" fill="var(--card-bg)"/>
    <circle cx="670" cy="410" r="85" fill="none" stroke="var(--ring)" stroke-width="30"/>
    <circle cx="40" cy="500" r="80" fill="none" stroke="var(--ring)" stroke-width="26"/>

    <rect class="bar bar--today" x="181" y="290" width="158" height="172" fill="url(#bar-teal)"/>
    <rect class="bar bar--30" x="339" y="262" width="147" height="200" fill="url(#bar-amber)"/>
    <rect class="bar bar--90" x="486" y="195" width="127" height="267" fill="url(#bar-red)"/>

    <g class="axes" stroke="var(--white)" stroke-width="2" fill="var(--white)">
      <line x1="119" y1="462" x2="119" y2="118"/>
      <polygon points="119,108 113,121 125,121" stroke="none"/>
      <line x1="119" y1="462" x2="670" y2="462"/>
      <polygon points="681,462 668,456 668,468" stroke="none"/>
    </g>
    <text class="axis-label" x="117" y="86" text-anchor="middle">Price</text>
    <text class="axis-label" x="654" y="498" text-anchor="middle">Time</text>

    <polygon class="trend-arrow" fill="url(#trend-left)"
      points="120,281 262,300 413,265 550,215 616,170 607,160 650,143 634,186 626,176 555,238 415,291 262,313 120,283"/>
    <text class="trend-label" x="621" y="122" text-anchor="middle">Price Trend</text>

    <text class="headline" x="260" y="206" text-anchor="middle">Signup Today</text>
    <text class="headline headline--strong" x="260" y="230" text-anchor="middle">for Huge Savings!</text>

    <circle cx="260" cy="307" r="52" fill="url(#teal-fill)" stroke="var(--white)" stroke-width="4"/>
    <text class="price" x="260" y="317" text-anchor="middle" fill="var(--white)" font-size="26">$ 6,500</text>
    <text class="stage-name" x="256" y="385" text-anchor="middle" fill="var(--white)" font-size="19">Today</text>
    <text class="stage-sub" x="256" y="406" text-anchor="middle" fill="var(--muted)" font-size="18">Price</text>

    <circle cx="413" cy="276" r="43" fill="url(#amber-fill)" stroke="#bdbdbd" stroke-width="3"/>
    <text class="price" x="413" y="284" text-anchor="middle" fill="#ecdcb8" font-size="20">$7,280</text>
    <text class="stage-name" x="413" y="347" text-anchor="middle" fill="#c8c8c8" font-size="16">30 Days</text>
    <text class="stage-sub" x="413" y="367" text-anchor="middle" fill="var(--dim)" font-size="15">Price</text>

    <circle cx="550" cy="229" r="37" fill="url(#red-fill)" stroke="#bdbdbd" stroke-width="3"/>
    <text class="price" x="550" y="236" text-anchor="middle" fill="#e0c4c6" font-size="17">$7,460</text>
    <text class="stage-name" x="549" y="292" text-anchor="middle" fill="#c8c8c8" font-size="14">90 Days</text>
    <text class="stage-sub" x="549" y="310" text-anchor="middle" fill="var(--dim)" font-size="14">Price</text>
  </g>

  <!-- Right panel: tag chart -->
  <g class="panel panel--tags">
    <rect x="780" y="0" width="779" height="554" fill="var(--right-bg)"/>

    <polygon class="trend-arrow" fill="url(#trend-right)"
      points="898,222 1039,249 1175,215 1300,173 1390,113 1383,98 1428,86 1418,130 1405,122 1302,190 1177,229 1039,258 898,223"/>
    <text class="trend-label trend-label--bold" x="1284" y="139" text-anchor="middle">Price Trend</text>

    <g class="connectors" stroke-width="1.5">
      <line x1="1039" y1="253" x2="1039" y2="286" stroke="var(--teal-1)"/>
      <line x1="1175" y1="222" x2="1175" y2="294" stroke="var(--orange)"/>
      <line x1="1300" y1="181" x2="1300" y2="300" stroke="#c0303c"/>
    </g>

    <rect class="tag tag--90" x="1244" y="300" width="118" height="105" rx="5" fill="url(#red-fill)"/>
    <rect class="tag tag--30" x="1117" y="295" width="127" height="115" rx="5" fill="url(#amber-fill)"/>
    <rect class="tag tag--today" x="960" y="286" width="157" height="132" rx="6" fill="url(#teal-fill)"/>

    <g class="nodes" fill="var(--white)" stroke-width="2">
      <circle cx="1039" cy="253" r="5" stroke="var(--teal-1)"/>
      <circle cx="1039" cy="286" r="5" stroke="#0e7f78"/>
      <circle cx="1175" cy="222" r="5" stroke="var(--orange)"/>
      <circle cx="1175" cy="294" r="5" stroke="#b8862a" fill="#e6b548"/>
      <circle cx="1300" cy="181" r="5" stroke="#c0303c"/>
      <circle cx="1300" cy="300" r="5" stroke="var(--white)" fill="#c0303c"/>
    </g>

    <text class="stage-name" x="1035" y="330" text-anchor="middle" fill="var(--white)" font-size="19">Today</text>
    <text class="stage-sub" x="1035" y="353" text-anchor="middle" fill="var(--white)" font-size="18">Price</text>
    <text class="price" x="1039" y="391" text-anchor="middle" fill="var(--white)" font-size="24">$ 6,500</text>

    <text class="stage-name" x="1175" y="330" text-anchor="middle" fill="var(--white)" font-size="16">30 Days</text>
    <text class="stage-sub" x="1175" y="349" text-anchor="middle" fill="var(--white)" font-size="15">Price</text>
    <text class="price" x="1175" y="386" text-anchor="middle" fill="var(--white)" font-size="21">$7,280</text>

    <text class="stage-name" x="1303" y="333" text-anchor="middle" fill="var(--white)" font-size="14">90 Days</text>
    <text class="stage-sub" x="1303" y="351" text-anchor="middle" fill="var(--white)" font-size="14">Price</text>
    <text class="price" x="1303" y="381" text-anchor="middle" fill="var(--white)" font-size="17">$7,460</text>

    <text class="headline" x="1039" y="454" text-anchor="middle">Signup Today</text>
    <text class="headline headline--strong" x="1039" y="478" text-anchor="middle">for Huge Savings!</text>
  </g>
</svg>
</body>
</html>
```